Business Card Design for boarding house accomodation business

I need a business card design for my Sydney based boarding house business accomodation. providing rooms for rent in Sydney Australia with shard bathroom and kitchen.
The front of card, are my details with details of head office and the rear of card to have details of locations providing rooms for rent.

Industry/Entity Type

Business

Contact Information for Business Card

Front of card details:
HOLLOWAY MANAGEMENT PTY LTD t/a
LINDFIELD'S GUEST HOUSE
ABN:52907318460
Daniel Kavanagh
48 Clement st
Newtown 2042
Mobile:0417386920
Email:daniel@lindfieldsguesthouse.example.au

Back of Card:
Locations:
-48 Clement st
Newtown 2042

-362 Harlow st
Erskineville 2043

-87 Fenwick st
Bondi 2026

-294 Ashcombe rd
Marrickville 2043

```html
<!DOCTYPE html>
<html lang="en">
<head>
<meta charset="utf-8">
<title>Holloway Management – Business Card</title>
<link href="https://fonts.googleapis.com/css2?family=Open+Sans:ital,wght@0,400;0,600;0,700;1,700&display=swap" rel="stylesheet">
<style>
  :root {
    --stage: #000000;
    --white: #ffffff;
    --green: #3a9a1e;
    --green-dark: #1f7a10;
    --green-deep: #1b6e0c;
    --green-light: #5fb83a;
    --ink: #222222;
    --grey: #666666;
    --abn: #2d6a1a;
  }
  * { box-sizing: border-box; margin: 0; padding: 0; }
  html, body {
    width: 1200px; height: 900px; overflow: hidden;
    background: var(--stage);
    font-family: "Open Sans", Arial, sans-serif;
  }
  .canvas { position: relative; width: 1200px; height: 900px; }

  .card {
    position: absolute; top: 275px; width: 477px; height: 293px;
    overflow: hidden; text-align: center;
  }
  .card-front {
    left: 116px; background: var(--white);
    border-radius: 0 46px 0 46px;
  }
  .card-back {
    left: 622px;
    border-radius: 46px 0 46px 0;
    background: radial-gradient(ellipse 60% 65% at 50% 45%, #45a826 0%, #2d8f18 55%, var(--green-deep) 100%);
    color: var(--white);
  }

  .line { position: absolute; left: 0; right: 0; }

  .holder-name { top: 17px; font-size: 17px; font-weight: 700; color: var(--green); letter-spacing: 0.3px; }
  .brand-mark {
    position: absolute; top: 45px; left: 50%; margin-left: -33px;
    width: 66px; height: 66px; border-radius: 50%; background: var(--green);
  }
  .company { top: 122px; font-size: 18.5px; font-weight: 700; color: var(--ink); letter-spacing: 0.4px; }
  .tagline {
    display: flex; align-items: center; justify-content: center; gap: 6px;
    font-size: 10.5px; letter-spacing: 0.4px;
  }
  .tagline::before, .tagline::after { content: ""; height: 1px; width: 68px; }
  .card-front .tagline { top: 142px; color: var(--grey); }
  .card-front .tagline::before, .card-front .tagline::after { background: linear-gradient(90deg, transparent, #999); }
  .card-front .tagline::after { background: linear-gradient(90deg, #999, transparent); }

  .abn { top: 169px; font-size: 13px; color: var(--ink); }
  .abn b { color: var(--abn); font-weight: 700; }
  .contact { font-size: 13px; color: var(--ink); display: flex; align-items: center; justify-content: center; gap: 4px; }
  .phone { top: 200px; }
  .email { top: 220px; }
  .contact svg { fill: var(--green); }

  .address-band {
    position: absolute; left: 0; right: 0; bottom: 0; height: 48px;
    background: linear-gradient(180deg, var(--green-light) 0%, var(--green) 45%, var(--green-dark) 100%);
    color: var(--white); font-size: 13px; line-height: 48px;
  }

  .back-company { top: 38px; font-size: 20.5px; font-weight: 700; letter-spacing: 0.5px; }
  .card-back .tagline { top: 62px; font-size: 12px; }
  .card-back .tagline::before { width: 90px; background: linear-gradient(90deg, transparent, rgba(255,255,255,.8)); }
  .card-back .tagline::after { width: 90px; background: linear-gradient(90deg, rgba(255,255,255,.8), transparent); }
  .locations-title { top: 117px; font-size: 21px; font-weight: 700; font-style: italic; }
  .location { font-size: 13px; font-weight: 600; }
  .loc-1 { top: 158px; }
  .loc-2 { top: 191px; }
  .loc-3 { top: 223px; }
  .loc-4 { top: 248px; }
</style>
</head>
<body>
<div class="canvas">

  <section class="card card-front">
    <p class="line holder-name">DANIEL KAVANAGH</p>
    <div class="brand-mark" aria-hidden="true"></div>
    <p class="line company">HOLLOWAY MANAGEMENT PTY LTD</p>
    <p class="line tagline">LINDFIELD'S GUEST HOUSE</p>
    <p class="line abn"><b>ABN:</b> 52907318460</p>
    <p class="line contact phone">
      <svg width="10" height="10" viewBox="0 0 24 24" aria-hidden="true"><path d="M6.6 10.8a15.1 15.1 0 0 0 6.6 6.6l2.2-2.2c.3-.3.7-.4 1-.2 1.1.4 2.3.6 3.6.6.6 0 1 .4 1 1V20c0 .6-.4 1-1 1A17 17 0 0 1 3 4c0-.6.4-1 1-1h3.5c.6 0 1 .4 1 1 0 1.3.2 2.5.6 3.6.1.3 0 .7-.2 1z"/></svg>
      0417386920
    </p>
    <p class="line contact email">
      <svg width="11" height="8" viewBox="0 0 22 16" aria-hidden="true"><path d="M0 0h22v16H0z M1.5 1.5 11 9l9.5-7.5z" fill-rule="evenodd"/></svg>
      daniel@lindfieldsguesthouse.example.au
    </p>
    <div class="address-band">48 Clement st Newtown 2042</div>
  </section>

  <section class="card card-back">
    <p class="line back-company">HOLLOWAY MANAGEMENT PTY LTD</p>
    <p class="line tagline">LINDFIELD'S GUEST HOUSE</p>
    <h2 class="line locations-title">Locations</h2>
    <p class="line location loc-1">48 Clement st Newtown 2042</p>
    <p class="line location loc-2">362 Harlow st Erskineville 2043</p>
    <p class="line location loc-3">87 Fenwick st Bondi 2026</p>
    <p class="line location loc-4">294 Ashcombe rd Marrickville 2043</p>
  </section>

</div>
</body>
</html>
```